Geschäftspapier-Design für Anbieter einer Online-Ausbildung für den qualifizierten Krankentransport und Rettungsdienst
Zielgruppe
LOTH Online-Ausbildung für den qualifizierten Krankentransport und Rettungsdienst
Der qualifizierte Krankentransport und Rettungsdienst ist zuständig für den Transport- und die Versorgung von kranken und verletzten Menschen. LOTH Medizinische Ausbildung und Seminare hat sich als Privatschule für die präklinische Notfallmedizin auf Aus- und Weiterbildungen im E-Learning-Modul für diese zwei Fachbereiche spezialisiert. Alle unsere Fachausbildungen sind online in unserem modernen Campus mit überregionalem Zugang absolvierbar.
Aufgabenstellung
Wir benötigen eine Word-Briefvorlage für den alltäglichen Geschäftsverkehr in drei Ausführungen.
- Briefvorlage mit Angabe der Abteilung -> Sekretariat
- Briefvorlage mit Angabe der Abteilung -> Schulleitung
- Briefvorlage mit Angabe der Abteilung -> Geschäftsführung
- Briefvorlage mit Angabe der Abteilung -> Buchhaltung/ Forderungsmanagement
Die Vorlage sollte bitte folgende Angaben aufweisen:
LOTH Bildungsgesellschaft UG (haftungsbeschränkt)
Privatschule für prähospitale Rettungsmedizin
Standort unserer Verwaltung:
Farnhügel 7
16248 Birkenwalde
Standort unseres Schulsitzes:
Am Quendelhof 48
D- 15537 Gosen- Neu Zittau
Schulleitung: Jutta Wildgrube & Matthias Lot
Ärztliche Leitung: Dr. Med. Ortwin Brasch
Pädagogische Leitung: Matthias Loth
Fachlicher Beirat: Dr. rer. med. Fabian Oswalt
Tel: 030 6270384 50
Fax: 030 6270384 51
E-Mail: info@loth-lehrwerkstatt.de
Web: www.loth-lehrwerkstatt.de
Vertreten durch: Jutta Wildgrube
Registereintrag: Eintragung im Handelsregister Registergericht: Amtsgericht Havelbrück Registernummer: HRB 27403 FF

```html
<!DOCTYPE html>
<html lang="de">
<head>
<meta charset="utf-8">
<title>LOTH Briefbogen – Buchhaltung</title>
<link href="https://fonts.googleapis.com/css2?family=Source+Sans+3:wght@400;600;700&display=swap" rel="stylesheet">
<style>
  :root {
    --brand-blue: #6ca6d6;
    --ink: #1a1a1a;
    --paper: #ffffff;
    --rule: #222222;
  }
  * { margin: 0; padding: 0; box-sizing: border-box; }
  html, body { width: 862px; height: 1200px; overflow: hidden; background: var(--paper); }
  body { font-family: "Source Sans 3", "Myriad Pro", sans-serif; color: var(--ink); position: relative; }

  .sheet-frame { position: absolute; left: 37px; top: 43px; width: 786px; height: 1107px; border: 1px solid var(--rule); }
  .band { position: absolute; left: 37px; width: 786px; height: 15px; background: var(--brand-blue); }
  .band--top { top: 58px; }
  .band--bottom { top: 1121px; }
  .hairline { position: absolute; left: 37px; width: 786px; height: 1px; background: var(--rule); }
  .hairline--top { top: 78px; }
  .hairline--bottom { top: 1115px; }

  .fold-mark { position: absolute; left: 37px; width: 15px; height: 1px; background: var(--rule); }
  .fold-mark--upper { top: 436px; }
  .fold-mark--lower { top: 599px; }
  .window-dot { position: absolute; width: 1.5px; height: 1.5px; background: var(--ink); top: 387px; }

  .brand-name { position: absolute; left: 494px; top: 130px; width: 88px; text-align: center;
    font-size: 30px; font-weight: 700; color: var(--brand-blue); letter-spacing: 1px; line-height: 1; }

  .info-column { position: absolute; left: 590px; top: 103px; height: 302px; border-left: 1px solid var(--brand-blue); }
  .info { position: absolute; left: 598px; font-size: 10.5px; line-height: 14px; white-space: nowrap; }
  .company { top: 126px; font-size: 12.5px; font-weight: 600; line-height: 15.5px; }
  .school-type { top: 161px; font-size: 12.5px; font-weight: 600; line-height: 15.5px; }
  .department { top: 210px; font-size: 13px; font-weight: 700; color: var(--brand-blue); line-height: 15px; }
  .department span { display: block; padding-left: 10px; }
  .department span:first-child { padding-left: 0; }
  .label { color: var(--brand-blue); }
  .admin { top: 244px; }
  .seat { top: 289px; }
  .phone { top: 333px; }
  .web { top: 363px; }

  .return-address { position: absolute; left: 138px; top: 220px; font-size: 10px; line-height: 12px;
    border-bottom: 1px solid var(--rule); padding-bottom: 2px; white-space: nowrap; }

  .footer-col { position: absolute; top: 1058px; height: 48px; border-left: 1px solid var(--brand-blue);
    padding-left: 8px; font-size: 8.5px; line-height: 12px; white-space: nowrap; }
  .footer-col .label { font-weight: 600; }
  .footer-col--team { left: 83px; }
  .footer-col--register { left: 339px; }
  .footer-col--bank { left: 590px; padding-left: 7px; }
</style>
</head>
<body>
  <div class="sheet-frame"></div>
  <div class="band band--top"></div>
  <div class="hairline hairline--top"></div>

  <div class="brand-name">LOTH</div>
  <div class="info-column"></div>

  <div class="info company">LOTH Bildungsgesellschaft UG<br>(haftungsbeschränkt)</div>
  <div class="info school-type">Privatschule für<br>prähospitale Rettungsmedizin</div>
  <div class="info department"><span>– Buchhaltung und</span><span>Forderungsmanagement –</span></div>
  <div class="info admin"><span class="label">Verwaltung:</span><br>Farnhügel 7<br>16248 Birkenwalde</div>
  <div class="info seat"><span class="label">Schulsitz:</span><br>Am Quendelhof 48<br>16248 Lindenau-Seefeld</div>
  <div class="info phone">Tel. 030&nbsp; 6270384 50<br>Fax 030&nbsp; 6270384 51</div>
  <div class="info web">E-Mail: info@loth-lehrwerkstatt.de<br>Web: www.loth-lehrwerkstatt.de</div>

  <div class="return-address">LOTH Bildungsgesellschaft UG&nbsp; | &nbsp;Farnhügel 7&nbsp; | &nbsp;16248 Birkenwalde</div>

  <div class="window-dot" style="left:112px"></div>
  <div class="window-dot" style="left:430px"></div>
  <div class="fold-mark fold-mark--upper"></div>
  <div class="fold-mark fold-mark--lower"></div>

  <div class="footer-col footer-col--team">
    <span class="label">Schulleitung:</span> Jutta Wildgrube · Matthias Loth<br>
    <span class="label">Ärztliche Leitung:</span> Dr. med. Ortwin Brasch<br>
    <span class="label">Pädagogische Leitung:</span> Matthias Loth<br>
    <span class="label">Fachlicher Beirat:</span> Dr. rer. med. Fabian Oswalt
  </div>
  <div class="footer-col footer-col--register">
    <span class="label">Vertreten durch:</span> Jutta Wildgrube<br>
    <span class="label">Registereintrag:</span> Eintragung im Handelsregister<br>
    <span class="label">Registergericht:</span> Amtsgericht Havelbrück<br>
    <span class="label">Registernummer:</span> HRB 27403 FF
  </div>
  <div class="footer-col footer-col--bank">
    <span class="label">Kontoverbindung:</span><br>
    Spreetaler Sparkasse<br>
    IBAN: DE00 0000 0000 0000 0000 00<br>
    BIC: XXXXXXXXXXX
  </div>

  <div class="hairline hairline--bottom"></div>
  <div class="band band--bottom"></div>
</body>
</html>
```